DATA PROTECTION OFFICER - GENERAL DATA PROTECTION REGULATION

Our network of companies is called : KVR (KVRL-MTO FLINTS).
It is sourced and based in Brussels, Belgium, hosting the EU institutions : designers and enforcers of the GDPR (https://portal.verimunda.example/info/norm/norm-topic/record-safety_en).
We are setting up connected, empowered and visionary-interconnected organizations in each country, region or city concerned by the GDPR.
We have developed unique pedagogical methods, programs, instruments (video, softwares,…) and visionary training skills – initially and on a continuous basis – for the DPO & GDPR consultants.
Our motto is : From Challenges to Opportunities.
Our yearning is : developing soulful teams, join forces & talents with our clients.
Our most wanted reward : let us astonish you!
We opt for the best available softwares on the market for project management, data analytics, GDPR compliance, DPO assistance and in general : customer relation and enhanced communication between project members.
We contribute to bringing Artificial Intelligence and Data-Driven Mindsets in enterprises.
We perceive the GDPR as the best opportunity an organization faces to value its “gold” (its data) and offer the solutions to transform them into real-life currencies and assets… MONEY .
I guess my comments need time to be integrated and I provided a lot of text too! I would particularly encourage TW (UK) to take the best out of his several proposals to mix them in the best ONE website! Offering me many graphic elements to use for all my posts/pages... I am a prolix writer :)
Target Market(s)
SME's business leaders, HR and Legal departments, read : https://www.corvanews.example/article/us-net-story-x1/growth-of-the-record-keeping-role-a-popular-new-career-path-idXQZT4LM8PW2K
Industry/Entity Type
Legal
Coding
Coded - Design and coding required
Number of Pages Required
5+ page
Colors
Designer to choose colors to be used in the design.
Requirements
Must have
- A HUMAN APPROACH
- WE NEED TO SEE HUMANS AND NOT ONLY ROBOTS OR ELECTRONIC DEVICES.
- 1) The DPO/GDPR Logos of the companies:
- https://www.filhaven.example/sh/k82q19wtzr4mn00/BXT7peLqVbZy0ghhwrR3Kslue?dl=0
- https://www.filhaven.example/sh/r3k27tjxwq85zmp/BXB4ktVRddh_q8ml5mtBgGqej?dl=0 et DPO : https://www.filhaven.example/sh/t9w4kjh7vcq48r2/BXJsmGZfRmYuvzIkwjR4Th_b?dl=0
- OR :
- https://www.filhaven.example/sh/vakkzp3mr5zgbn/BXBTxCRQ4lXmEFWN3LRg3kR7b?dl=0
- AND :
- https://stewardmesh.docushelf.example/sites/all/_layouts/15/visitorlink.aspx?visitortoken=Q4xbbe862KMTW7HkfaM5Wq0r%2BTcnNvdj1tqKX%2FmUmQOV%3D&folderid=3_2f70b91a29a805d81c96b8636e419f7ce&rev=1&e=6b600bf144535597b9296c99cd6116c9
- 2) A surprising but human, clear, simple, white, lightning look!
- 3) WORDPRESS version so that I can edit easily and add text on existing and new pages
- We therefore pass each option and - even more so - through the sieve of this inevitable - and values-generating - ethical evaluation.
- In other words, we are doubly satisfied with EVERY solution:
- 1. As a DPO/consultant and advisor to commercial enterprises or non-profit organisations but necessarily entering into a relationship involving financial flows with the persons concerned; and
- 2. As concerned person: target of the actions envisaged, parent, child, citizen and avatar in our digital lives.
- We put personal data at the centre of our projects and internal meetings, and with clients, we therefore continue the stage of brainstorming, researching and visualising ideas in interaction with the Regulation, by analysing the ethical consequences of each option.
- We choose only solutions that are applicable to the greatest number and therefore satisfy us as citizens of an increasingly connected and digital world. We also see the Regulation as a commercial and marketing opportunity to enhance the value of personal data and develop the confidence of those concerned by respect and security in the processing of such data.
- Our ultimate test: we put ourselves in our children's shoes to test the option considered, then comment on it and evaluate it as a parent.
- NO TO INCOMPREHENSIVE LEGAL TERMS... It is simply prohibited from 25 May for all information to be communicated to the persons concerned by the Regulation!
Nice to have
- - Artificial Intelligence
- - Transhumans
- - Challenges becoming Opportunities
- - a Great Dame who Protects & Reassures (see GDPR logo)
- - Friendly communication - NOT too businesslike/cold/usual
- - Page content is available here in FRENCH then ENGLISH then DUTCH then GERMAN : https://www.filhaven.example/sh/w1hjqmzsa101zwv/BXDNsFZpQSEzpMjhvRr5ZCb?dl=0
Should not have
- A cold, bankerlike, old economy, dull outlook

```html
<!DOCTYPE html>
<html lang="en">
<head>
<meta charset="utf-8">
<title>KVR – Data Analytics, GDPR Compliance and DPO Assistance</title>
<link rel="stylesheet" href="https://fonts.googleapis.com/css2?family=Montserrat:wght@400;500;600&family=Open+Sans:wght@400;600&family=Lato:wght@700;900&display=swap">
<style>
  :root{
    --magenta:#a2236f;
    --magenta-deep:#951a68;
    --plum:#7f1a5c;
    --coral:#e3796b;
    --peach:#f2ad90;
    --rose:#cc4f8e;
    --navy:#03172e;
    --navy-2:#0a2f52;
    --cyan:#2fb7e8;
    --ink:#3c3c3c;
    --body:#555a60;
    --mist:#e9c6dc;
    --white:#ffffff;
  }
  *{margin:0;padding:0;box-sizing:border-box}
  html,body{width:1200px;height:3114px;overflow:hidden;background:var(--white)}
  body{position:relative;font-family:"Open Sans",Arial,sans-serif;color:var(--body)}
  .abs{position:absolute}

  /* header */
  .site-header{position:absolute;left:0;top:0;width:1200px;height:110px;background:var(--white)}
  .brand{position:absolute;left:122px;top:22px;display:flex;align-items:center;gap:14px}
  .brand-mark{width:22px;height:22px;background:var(--magenta);border-radius:50%}
  .brand-name{font-family:"Montserrat",sans-serif;font-weight:600;font-size:38px;color:var(--magenta);letter-spacing:1px}
  .main-nav a{position:absolute;top:46px;font-family:"Montserrat",sans-serif;font-weight:500;font-size:16px;color:var(--ink);text-decoration:none;white-space:nowrap}
  .main-nav a.is-active{color:var(--magenta)}

  /* hero */
  .hero{position:absolute;left:0;top:110px;width:1200px;height:580px;background:radial-gradient(ellipse at 28% 40%,var(--navy-2) 0%,var(--navy) 60%);overflow:hidden}
  .hero-art{position:absolute;left:80px;top:0;width:470px;height:520px;background:radial-gradient(ellipse at 55% 45%,rgba(47,183,232,.75) 0%,rgba(20,110,170,.45) 45%,rgba(3,23,46,0) 75%)}
  .hero-title{position:absolute;left:654px;top:150px;width:420px;font-family:"Montserrat",sans-serif;font-weight:500;font-size:35px;line-height:45px;color:var(--white);letter-spacing:.5px}
  .hero-text{position:absolute;left:654px;top:300px;width:400px;font-size:15px;line-height:24px;color:#e3e9f0}
  .slider-dots{position:absolute;left:548px;top:447px;display:flex;align-items:center;gap:6px}
  .slider-dots .arrow{width:18px;height:18px;border-radius:50%;background:var(--white)}
  .slider-dots .dot{width:9px;height:9px;border-radius:50%;background:#8a96a6}
  .slider-dots .dot.is-on{background:var(--white)}
  .hero-edge{position:absolute;left:0;bottom:0}

  /* about */
  .about-art{left:660px;top:695px;width:420px;height:436px;background:radial-gradient(ellipse at 55% 55%,#c9ced6 0%,#e8eaee 42%,rgba(255,255,255,0) 70%)}
  .about-title{left:143px;top:757px;font-family:"Montserrat",sans-serif;font-weight:500;font-size:34px;color:var(--magenta);letter-spacing:1px}
  .about-copy{left:143px;top:816px;width:505px;font-size:14.5px;line-height:20px;color:var(--body);z-index:2}
  .about-copy p{margin-bottom:14px}
  .btn-outline{left:141px;top:1053px;width:148px;height:42px;border:2px solid var(--magenta);color:var(--magenta);font-family:"Montserrat",sans-serif;font-weight:600;font-size:15px;display:flex;align-items:center;justify-content:center}

  /* pillars */
  .pillars{position:absolute;left:0;top:1214px;width:1200px;height:484px;background:linear-gradient(100deg,var(--peach) 0%,#e27d8f 45%,var(--rose) 100%);overflow:hidden}
  .pillar{position:absolute;top:38px;width:304px;height:304px;border-radius:50%;background:rgba(190,60,110,.28);text-align:center;color:var(--white)}
  .pillar-icon{margin:110px auto 0;width:86px;height:86px;border-radius:50%;background:rgba(255,255,255,.22)}
  .pillar-title{position:absolute;top:212px;left:0;width:100%;font-family:"Montserrat",sans-serif;font-weight:500;font-size:22px}
  .pillar-text{position:absolute;top:246px;left:52px;width:200px;font-size:12.5px;line-height:18px;color:#fbe3ec}
  .pillars-ridge{position:absolute;left:0;bottom:0}

  /* how it works */
  .section-title{left:0;top:1763px;width:1200px;text-align:center;font-family:"Montserrat",sans-serif;font-weight:500;font-size:24px;color:var(--coral);letter-spacing:1px}
  .step{position:absolute}
  .step-head{display:flex;align-items:baseline;gap:10px;font-family:"Lato",sans-serif}
  .step-num{font-weight:900;font-size:44px;color:var(--coral);line-height:1}
  .step-name{font-weight:900;font-size:26px;color:#3a3a3a;line-height:30px}
  .step-body{margin-top:14px;font-size:14.5px;line-height:20px;color:var(--body)}
  .step-body p{margin-bottom:14px}
  .step-art{position:absolute;opacity:.9}
  .art-monitor{left:208px;top:1900px;width:207px;height:213px;border-radius:14px;background:linear-gradient(180deg,#a8336f 0%,#8e1e62 100%)}
  .art-network{left:714px;top:2252px;width:200px;height:200px;border-radius:50%;background:radial-gradient(circle,#b0407f 0%,#8e1e62 70%)}
  .art-rings{left:166px;top:2553px;width:250px;height:250px;border-radius:50%;background:radial-gradient(circle,#a23a7b 0%,#8e1e62 70%)}
  .connectors{position:absolute;left:0;top:1800px}

  /* footer */
  .footer-ridge{position:absolute;left:0;top:2860px}
  .site-footer{position:absolute;left:0;top:2958px;width:1200px;height:156px;background:var(--magenta-deep)}
  .footer-nav a{position:absolute;top:50px;font-family:"Montserrat",sans-serif;font-weight:600;font-size:16px;color:var(--white);text-decoration:none;white-space:nowrap}
  .copyright{position:absolute;left:122px;top:84px;font-size:12px;color:#e2b6d2}
  .social{position:absolute;top:50px;width:22px;height:22px;border-radius:50%;background:var(--white)}
</style>
</head>
<body>

<header class="site-header">
  <div class="brand"><span class="brand-mark"></span><span class="brand-name">KVR</span></div>
  <nav class="main-nav">
    <a class="is-active" style="left:430px">Home</a>
    <a style="left:506px">About Us</a>
    <a style="left:610px">How it Works</a>
    <a style="left:743px">Resources</a>
    <a style="left:855px">Our Services</a>
    <a style="left:985px">Contact Us</a>
  </nav>
</header>

<section class="hero">
  <div class="hero-art" role="img" aria-label="Glowing digital circuit-board profile of a human head in blue"></div>
  <h1 class="hero-title">Data Analytics, GDPR Compliance and DPO Assistance</h1>
  <p class="hero-text">Class aptent taciti sociosqu ad litora torquent pear conubia nostra per inceptos</p>
  <div class="slider-dots">
    <span class="arrow"></span><span class="dot is-on"></span><span class="dot"></span><span class="dot"></span><span class="dot"></span><span class="arrow"></span>
  </div>
  <svg class="hero-edge" width="1200" height="110" viewBox="0 0 1200 110" aria-hidden="true">
    <path d="M0 110 L0 88 L300 60 L460 56 L560 38 L600 2 L640 22 L700 28 L820 44 L960 50 L1040 60 L1200 92 L1200 110 Z" fill="#ffffff"/>
  </svg>
</section>

<div class="abs about-art" role="img" aria-label="Low-poly wireframe illustration of a human head dissolving into triangles"></div>
<h2 class="abs about-title">ABOUT US</h2>
<div class="abs about-copy">
  <p>Our network of companies is called : KVR (KVRL-MTO FLINTS).</p>
  <p>It is sourced and based in Brussels, Belgium, hosting the EU institutions : designers and enforcers of the GDPR (https://portal.verimunda.example/info/norm/norm-topic/record-safety_en).</p>
  <p>We are setting up connected, empowered and visionary-interconnected organizations in each country, region or city concerned by the GDPR. We have developed unique pedagogical methods, programs, instruments (video, softwares,…) and visionary training skills – initially and on a continuous basis – for the DPO &amp; GDPR consultants.</p>
</div>
<a class="abs btn-outline">Learn More</a>

<section class="pillars">
  <div class="pillar" style="left:110px">
    <div class="pillar-icon" role="img" aria-label="Legal document icon"></div>
    <h3 class="pillar-title">Legal Design</h3>
    <p class="pillar-text">Class aptent taciti sociosqu ad litora torquent per co</p>
  </div>
  <div class="pillar" style="left:448px">
    <div class="pillar-icon" role="img" aria-label="Artificial intelligence icon"></div>
    <h3 class="pillar-title">Artificial Intelligence</h3>
    <p class="pillar-text">Class aptent taciti sociosqu ad litora torquent per co</p>
  </div>
  <div class="pillar" style="left:785px">
    <div class="pillar-icon" role="img" aria-label="Caring hands icon"></div>
    <h3 class="pillar-title">Human by Design</h3>
    <p class="pillar-text">Class aptent taciti sociosqu ad litora torquent per co</p>
  </div>
  <svg class="pillars-ridge" width="1200" height="130" viewBox="0 0 1200 130" aria-hidden="true">
    <path d="M0 130 L0 60 L90 40 L150 56 L200 30 L300 50 L420 58 L520 72 L620 44 L700 60 L820 58 L980 40 L1060 20 L1130 40 L1200 30 L1200 130 Z" fill="#c85a78" opacity=".55"/>
  </svg>
</section>

<h2 class="abs section-title">HOW IT WORKS</h2>

<svg class="connectors" width="1200" height="1000" viewBox="0 1800 1200 1000" aria-hidden="true">
  <path d="M415 2060 C520 2040 560 2140 600 2200 C640 2270 690 2290 720 2300" fill="none" stroke="#777" stroke-width="2" stroke-dasharray="6 5"/>
  <path d="M720 2420 C640 2430 580 2480 540 2560 C500 2640 470 2680 420 2678" fill="none" stroke="#777" stroke-width="2" stroke-dasharray="6 5"/>
</svg>

<div class="step-art art-monitor" role="img" aria-label="Monitor icon showing a pie chart and list"></div>
<article class="step" style="left:556px;top:1870px;width:430px">
  <div class="step-head"><span class="step-num">01</span><span class="step-name">GRAPHIC TABLE &amp;<br>INTERACTION</span></div>
  <div class="step-body" style="padding-left:11px">
    <p>The 3 profiles of our teams (IT/cybersecurity Expert - Lawyer - Project Manager) make use of modern tools of communication INTERNALLY and EXTERNALLY: with external clients and partners.</p>
    <p>We use tactile tablets and graphic applications for drawing, mind-mapping, visualization, advanced natural language generation (advanced NLG), video, storytelling,....</p>
  </div>
</article>

<article class="step" style="left:116px;top:2232px;width:480px">
  <div class="step-head"><span class="step-num">02</span><span class="step-name">HUMAN BY DESIGN</span></div>
  <div class="step-body" style="padding-left:6px">
    <p>EACH solution passes a double test that satisfies us both :</p>
    <p>1. As a DPO/consultant and advisor to commercial enterprises or non-profit organizations but necessarily entering into a relationship involving financial flows with the persons concerned; and</p>
    <p>2. As a data subject : "target" of the envisaged actions, parent, child, citizen and avatar in our digital lives.</p>
  </div>
</article>
<div class="step-art art-network" role="img" aria-label="Network icon of a person connected to surrounding nodes"></div>

<div class="step-art art-rings" role="img" aria-label="Concentric arcs icon"></div>
<article class="step" style="left:565px;top:2628px;width:500px">
  <div class="step-head"><span class="step-num">03</span><span class="step-name">VISUALIZATION AND REDACTION</span></div>
  <div class="step-body" style="padding-left:2px">
    <p>During the first two stages, we prepared a desirable objective:<br>Communicate visually after an ethical check.</p>
    <p>Two external solutions (human and artificial) will help us to finalize the communication in a professional and optimal way:</p>
  </div>
</article>

<svg class="footer-ridge" width="1200" height="100" viewBox="0 0 1200 100" aria-hidden="true">
  <path d="M0 100 L0 50 L110 38 L170 10 L250 40 L420 44 L560 50 L700 40 L840 42 L960 30 L1060 8 L1130 28 L1200 38 L1200 100 Z" fill="#e9c6dc"/>
</svg>

<footer class="site-footer">
  <nav class="footer-nav">
    <a style="left:122px">Home</a>
    <a style="left:198px">About Us</a>
    <a style="left:302px">How it Works</a>
    <a style="left:436px">Resources</a>
    <a style="left:547px">Our Services</a>
    <a style="left:678px">Contact Us</a>
  </nav>
  <p class="copyright">© 2018 Company Name. All right reserved</p>
  <span class="social" style="left:942px" role="img" aria-label="Social link"></span>
  <span class="social" style="left:988px" role="img" aria-label="Social link"></span>
  <span class="social" style="left:1036px" role="img" aria-label="Social link"></span>
</footer>

</body>
</html>
```